Design Shopify E-Commerce Website for Men's Products

Design a Shopify website for men to sell our men's jewelry, cigar and bar accessories, and other men's products. Design should be hip, with like a rock n' roll, biker, whiskey driker flare. Name of the company is "Ironvale Locker" and website will be www.IronvaleLocker.com
Homepage will have navigation bar with three categories: Men's Jewelry, Cigar & Bar Products, Man Cave Swag
I will upload our logo, inspiration type pictures and some of the products that we sell
Theme colors should be mainly dark: black, grey, brown, gold

```html
<!DOCTYPE html>
<html lang="en">
<head>
<meta charset="utf-8">
<title>Ironvale Locker — Men's Jewelry, Cigar &amp; Bar Products, Man Cave Swag</title>
<link href="https://fonts.googleapis.com/css2?family=Barlow+Semi+Condensed:wght@500;600;700&family=Montserrat:wght@400;500;600;700&display=swap" rel="stylesheet">
<style>
:root{
  --black:#0e0e0e;
  --coal:#161616;
  --card:#1c1c1c;
  --grey:#5b5b5b;
  --light:#ebebeb;
  --white:#ffffff;
  --gold:#d6b04a;
  --gold-dark:#a98427;
  --gold-soft:#e3c660;
  --brown:#5a3a1e;
  --muted:#9a9a9a;
  --head:"Barlow Semi Condensed",sans-serif;
  --body:"Montserrat",sans-serif;
}
*{box-sizing:border-box;margin:0;padding:0}
html,body{width:1200px;height:4216px;overflow:hidden}
body{position:relative;background:var(--black);font-family:var(--body);color:var(--white)}
.abs{position:absolute}
.photo{position:absolute}
.h{font-family:var(--head);font-weight:700;text-transform:uppercase;letter-spacing:1px}
.copy{font-size:10.5px;line-height:1.75;color:#d8d8d8}
.btn-gold{position:absolute;display:flex;align-items:center;justify-content:center;background:linear-gradient(90deg,var(--gold-dark),var(--gold-soft),var(--gold-dark));color:#111;font-weight:700;font-size:12px}
.btn-line{position:absolute;display:flex;align-items:center;justify-content:center;border:1px solid #bdbdbd;font-size:12px}

/* header */
.brand{left:80px;top:40px;display:flex;align-items:center;gap:8px;font-family:var(--head);font-weight:700;font-size:20px;color:var(--gold);text-transform:uppercase}
.brand i{width:14px;height:14px;border-radius:50%;background:var(--gold);display:block}
.nav a{position:absolute;top:25px;font-size:11.5px;font-weight:600;color:var(--white);text-decoration:none}
.nav a.active{color:var(--gold)}
.icon{position:absolute;top:22px;width:22px;height:22px}

/* hero */
.hero{left:0;top:0;width:1200px;height:617px;background:radial-gradient(ellipse at 75% 40%,#2b2418 0%,#141414 55%,#0c0c0c 100%)}
.ring{left:565px;top:122px;width:410px;height:410px;border-radius:50%;border:30px solid var(--gold)}
.hero-photo{left:610px;top:55px;width:590px;height:562px;background:radial-gradient(ellipse at 45% 40%,rgba(120,96,70,.75),rgba(50,40,32,.55) 45%,rgba(20,20,20,0) 75%)}
.hero-title{left:123px;top:150px;font-size:70px;line-height:70px;letter-spacing:2px}
.hero-title span{color:var(--gold)}

/* categories */
.tile-label{position:absolute;top:1056px;height:62px;width:395px;background:#ececec;color:#111;display:flex;align-items:center;justify-content:center;font-size:22px}

/* featured */
.featured{left:0;top:1126px;width:1200px;height:629px;background:var(--light)}
.pcard{position:absolute;top:1339px;width:230px;height:277px;background:var(--white)}
.pname{position:absolute;font-family:var(--head);font-weight:600;font-size:14px;color:#111;text-transform:uppercase;letter-spacing:.6px}
.psub{position:absolute;font-size:9.5px;color:#666}
.pprice{position:absolute;font-size:13px;font-weight:700;color:#111}
.circle{position:absolute;width:34px;height:34px;border-radius:50%;background:var(--white);display:flex;align-items:center;justify-content:center;box-shadow:0 1px 4px rgba(0,0,0,.25)}
.heart{position:absolute;width:18px;height:18px}

/* popular */
.pop{position:absolute;top:1880px;width:293px;height:458px;background:var(--card)}
.pop .photo{left:0;top:0;width:293px;height:358px}
.pop .pn{position:absolute;left:18px;top:372px;font-family:var(--head);font-weight:600;font-size:14px;letter-spacing:.6px}
.pop .pp{position:absolute;right:18px;top:372px;font-size:13px;font-weight:700}
.pop .add{position:absolute;left:18px;top:408px;width:257px;height:32px;border:1px solid #d0d0d0;display:flex;align-items:center;justify-content:center;font-size:12px;font-weight:500}
.pop .add.on{background:var(--gold);border-color:var(--gold);color:#111;font-weight:700}

/* testimonials */
.tcard{position:absolute;top:2968px;width:399px;height:216px;padding:36px 28px}
.tcard p{font-size:10px;line-height:1.8;color:#e2e2e2}
.avatar{position:absolute;left:28px;top:126px;width:46px;height:46px;border-radius:50%;background:radial-gradient(circle,#a77b5a,#5a3a28)}
.who{position:absolute;left:93px;top:134px;font-size:11px;font-weight:700}
.role{position:absolute;left:93px;top:154px;font-size:10.5px;color:var(--gold)}
.quote{position:absolute;right:28px;top:126px;font-family:Georgia,serif;font-size:64px;line-height:1;color:var(--gold-dark)}

/* how it works */
.step{position:absolute;top:3395px;width:200px;text-align:center}
.step svg{width:44px;height:44px;display:block;margin:0 auto}
.step h3{font-family:var(--head);font-weight:700;font-size:16px;letter-spacing:1px;margin-top:12px}
.step p{font-size:10px;line-height:1.5;color:#cfcfcf;margin-top:8px}

/* newsletter */
.news{left:0;top:3593px;width:1200px;height:306px;background:radial-gradient(ellipse at 30% 40%,#cfa93e,#dcbb52 55%,#d4b04a)}
.field{position:absolute;top:3755px;width:246px;height:30px;background:rgba(255,255,255,.22);font-size:10px;padding:9px 12px;color:#222}

/* footer */
.fhead{position:absolute;top:3944px;font-size:10.5px;font-weight:700;color:var(--gold);text-transform:uppercase}
.flink{position:absolute;font-size:11px;color:#e6e6e6}
.fdot{position:absolute;width:10px;height:10px;background:var(--gold)}
</style>
</head>
<body>

<!-- HERO -->
<section class="abs hero" aria-label="Hero">
  <div class="abs ring" aria-hidden="true"></div>
  <div class="photo hero-photo" role="img" aria-label="Bearded man in a cap exhaling a cloud of cigar smoke"></div>
  <div class="abs brand"><i></i>Ironvale Locker</div>
  <nav class="nav">
    <a class="active" style="left:309px">Home</a>
    <a style="left:386px">Men's Jewelry</a>
    <a style="left:511px">Cigar &amp; Bar Products</a>
    <a style="left:676px">Man Cave Swag</a>
    <a style="left:815px">Contact Us</a>
  </nav>
  <svg class="icon" style="left:957px" viewBox="0 0 24 24" fill="none" stroke="#d6b04a" stroke-width="2"><circle cx="10" cy="10" r="7"/><path d="M15 15l6 6"/></svg>
  <svg class="icon" style="left:1004px" viewBox="0 0 24 24" fill="none" stroke="#d6b04a" stroke-width="2"><circle cx="12" cy="8" r="4"/><path d="M4 21c1-5 4-7 8-7s7 2 8 7"/></svg>
  <svg class="icon" style="left:1046px" viewBox="0 0 24 24" fill="none" stroke="#d6b04a" stroke-width="2"><path d="M2 3h3l3 12h11l2-8H6"/><circle cx="9" cy="20" r="1.5"/><circle cx="18" cy="20" r="1.5"/></svg>
  <div class="abs" style="left:1063px;top:17px;width:14px;height:14px;border-radius:50%;background:#c8201e;font-size:8px;display:flex;align-items:center;justify-content:center">1</div>
  <h1 class="abs h hero-title">Shop <span>Our</span><br><span>Latest</span> New<br>Styles</h1>
  <p class="abs copy" style="left:123px;top:372px;width:335px">Lorem ipsum dolor sit amet, consectetur adipiscing elit, sed do eiusmod tempor incididunt ut labore et dolore magna aliqua. Quis ipsum suspendisse ultrices gravida. Risus commodo viverra maecenas accumsan lacus vel facilisis.</p>
  <div class="btn-gold" style="left:123px;top:465px;width:134px;height:38px">Shop Now</div>
</section>

<!-- CATEGORIES -->
<section aria-label="Categories">
  <div class="photo" style="left:0;top:622px;width:395px;height:434px;background:linear-gradient(160deg,#8a5a24,#6b4319 60%,#a06a2a)" role="img" aria-label="Silver cross jewelry, rings and chain bracelets on wood"></div>
  <div class="tile-label h" style="left:0">Men's Jewelry</div>
  <div class="photo" style="left:401px;top:622px;width:398px;height:496px;background:radial-gradient(ellipse at 50% 40%,#4a3424,#1d1610 70%)" role="img" aria-label="Glass of whiskey beside a cigar in low light"></div>
  <div class="abs" style="left:415px;top:636px;width:371px;height:470px;border:1px solid #9a9a9a"></div>
  <div class="abs h" style="left:401px;top:968px;width:398px;text-align:center;font-size:23px">Cigar &amp; Bar Products</div>
  <div class="btn-gold" style="left:534px;top:1018px;width:134px;height:36px">Shop Now</div>
  <div class="photo" style="left:804px;top:622px;width:396px;height:434px;background:linear-gradient(135deg,#3a2a20,#151515 55%,#e4e4e4 56%,#cfcfcf 70%,#1a1a1a 71%)" role="img" aria-label="Hand fastening a cufflink on a white shirt cuff"></div>
  <div class="tile-label h" style="left:804px;width:396px">Man Cave Swag</div>
</section>

<!-- FEATURED -->
<section class="abs featured" aria-label="Featured products"></section>
<div class="photo" style="left:18px;top:1144px;width:516px;height:591px;background:linear-gradient(180deg,#3a2620,#2a1c18 50%,#c9b48c 51%,#b49c74)" role="img" aria-label="Man in sunglasses and a beige trench coat against a brick wall"></div>
<h2 class="abs h" style="left:609px;top:1166px;font-size:37px;color:#111;letter-spacing:2px">Featured Products</h2>
<p class="abs copy" style="left:611px;top:1218px;width:420px;color:#444;font-size:10px">Lorem ipsum dolor sit amet, consectetur adipiscing elit, sed do eiusmod tempor incididunt ut labore et dolore magna aliqua. Quis ipsum suspendisse ultrices gravida. Risus commodo viverra maecenas accumsan lacus vel facilisis.</p>
<div class="btn-line" style="left:611px;top:1277px;width:134px;height:38px;border-color:#555;color:#222">Shop Now</div>

<div class="pcard" style="left:611px"><div class="photo" style="left:35px;top:60px;width:160px;height:150px;background:radial-gradient(circle,#d9c06a,#6d6d6d 55%,#fff 72%)" role="img" aria-label="Black and gold heavy ring"></div></div>
<div class="pcard" style="left:855px"><div class="photo" style="left:25px;top:70px;width:180px;height:120px;background:linear-gradient(180deg,#a8323a,#6e1418)" role="img" aria-label="Red cigar humidor with glass lid"></div></div>
<div class="pcard" style="left:1097px;width:103px"><div class="photo" style="left:20px;top:60px;width:83px;height:120px;background:radial-gradient(circle,#8a8a8a,#fff 70%)" role="img" aria-label="Silver pendant"></div></div>
<svg class="heart" style="left:812px;top:1350px" viewBox="0 0 24 24" fill="none" stroke="#999" stroke-width="1.6"><path d="M12 20s-7-4.5-7-10a4 4 0 0 1 7-2.5A4 4 0 0 1 19 10c0 5.5-7 10-7 10z"/></svg>
<svg class="heart" style="left:1056px;top:1350px" viewBox="0 0 24 24" fill="none" stroke="#999" stroke-width="1.6"><path d="M12 20s-7-4.5-7-10a4 4 0 0 1 7-2.5A4 4 0 0 1 19 10c0 5.5-7 10-7 10z"/></svg>
<div class="circle" style="left:566px;top:1461px"><svg width="12" height="12" viewBox="0 0 12 12"><path d="M8 1L3 6l5 5" fill="none" stroke="#222" stroke-width="1.5"/></svg></div>
<div class="circle" style="left:1152px;top:1461px"><svg width="12" height="12" viewBox="0 0 12 12"><path d="M4 1l5 5-5 5" fill="none" stroke="#222" stroke-width="1.5"/></svg></div>

<div class="pname" style="left:611px;top:1633px">Heavy Ring</div>
<div class="psub" style="left:611px;top:1657px">Black golden ring</div>
<div class="pprice" style="left:611px;top:1677px">$200.00</div>
<div class="pname" style="left:855px;top:1633px">Cigar Humidor</div>
<div class="psub" style="left:855px;top:1657px">Cigar box</div>
<div class="pprice" style="left:855px;top:1677px">$540.00</div>
<div class="pname" style="left:1097px;top:1633px">Pendantresize</div>
<div class="psub" style="left:1097px;top:1657px">Pendant</div>
<div class="pprice" style="left:1097px;top:1677px">$170.00</div>

<!-- POPULAR -->
<section aria-label="Popular products">
  <div class="abs" style="left:0;top:1755px;width:1200px;height:602px;background:var(--coal)"></div>
  <svg class="abs" style="left:214px;top:1808px" width="14" height="18" viewBox="0 0 14 18"><path d="M10 2L3 9l7 7" fill="none" stroke="#777" stroke-width="1.5"/></svg>
  <h2 class="abs h" style="left:0;top:1794px;width:1200px;text-align:center;font-size:36px;letter-spacing:2px">Popular Products</h2>
  <div class="abs" style="left:962px;top:1801px;width:34px;height:34px;border-radius:50%;background:#4a4a4a;display:flex;align-items:center;justify-content:center"><svg width="12" height="12" viewBox="0 0 12 12"><path d="M4 1l5 5-5 5" fill="none" stroke="#ddd" stroke-width="1.5"/></svg></div>

  <div class="pop" style="left:0"><div class="photo" style="background:linear-gradient(150deg,#8b5a30,#5a3a1e 55%,#f2f2f2 56%,#fff)" role="img" aria-label="Wooden whiskey set crate with glasses and stones"></div><div class="pn">WHISKEY SET</div><div class="pp">$540.00</div><div class="add">Add To Cart</div></div>
  <div class="pop" style="left:303px"><div class="photo" style="background:linear-gradient(180deg,#b07a3c,#7a4b1c 55%,#c08a40)" role="img" aria-label="Open wooden cigar box filled with cigars"></div><div class="pn">CIGAR BOX</div><div class="pp">$300.00</div><div class="add on">Add To Cart</div></div>
  <div class="pop" style="left:605px"><div class="photo" style="background:radial-gradient(circle at 50% 55%,#8a4a24,#4a2a14 45%,#f4f4f4 62%)" role="img" aria-label="Wooden desktop cigar cutter"></div><div class="pn">CIGARCUTTER</div><div class="pp">$420.00</div><div class="add">Add To Cart</div></div>
  <div class="pop" style="left:908px;width:292px"><div class="photo" style="width:292px;background:linear-gradient(160deg,#8a7a66,#5b4e40 50%,#9a8a76)" role="img" aria-label="Pair of silver cufflinks on weathered wood"></div><div class="pn">HEAVY RING</div><div class="pp">$200.00</div><div class="add">Add To Cart</div></div>
  <svg class="heart" style="left:256px;top:1895px;width:22px;height:22px" viewBox="0 0 24 24" fill="none" stroke="#888" stroke-width="1.4"><path d="M12 20s-7-4.5-7-10a4 4 0 0 1 7-2.5A4 4 0 0 1 19 10c0 5.5-7 10-7 10z"/></svg>
  <svg class="heart" style="left:860px;top:1895px;width:22px;height:22px" viewBox="0 0 24 24" fill="none" stroke="#888" stroke-width="1.4"><path d="M12 20s-7-4.5-7-10a4 4 0 0 1 7-2.5A4 4 0 0 1 19 10c0 5.5-7 10-7 10z"/></svg>
  <svg class="heart" style="left:1163px;top:1895px;width:22px;height:22px" viewBox="0 0 24 24" fill="none" stroke="#888" stroke-width="1.4"><path d="M12 20s-7-4.5-7-10a4 4 0 0 1 7-2.5A4 4 0 0 1 19 10c0 5.5-7 10-7 10z"/></svg>
</section>

<!-- NEW ARRIVALS -->
<section aria-label="New arrivals">
  <div class="abs" style="left:0;top:2357px;width:604px;height:472px;background:#141414"></div>
  <div class="photo" style="left:604px;top:2357px;width:596px;height:472px;background:linear-gradient(120deg,#2a2a2a,#8a8a8a 35%,#1a1a1a 60%,#b0b0b0 80%,#222)" role="img" aria-label="Black and white close-up of a chrome motorcycle"></div>
  <h2 class="abs h" style="left:121px;top:2484px;font-size:36px;letter-spacing:2px">New Arrivals</h2>
  <p class="abs copy" style="left:123px;top:2550px;width:335px">Lorem ipsum dolor sit amet, consectetur adipiscing elit, sed do eiusmod tempor incididunt ut labore et dolore magna aliqua. Quis ipsum suspendisse ultrices gravida. Risus commodo viverra maecenas accumsan lacus vel facilisis.</p>
  <div class="btn-gold" style="left:123px;top:2659px;width:170px;height:36px">DISCOVER NOW</div>
</section>

<!-- TESTIMONIALS -->
<section aria-label="Testimonials">
  <div class="abs" style="left:0;top:2829px;width:1200px;height:417px;background:var(--light)"></div>
  <h2 class="abs h" style="left:123px;top:2883px;font-size:36px;color:#111;letter-spacing:1.5px">What Our Clients Say</h2>
  <svg class="abs" style="left:578px;top:2896px" width="12" height="16" viewBox="0 0 12 16"><path d="M9 2L3 8l6 6" fill="none" stroke="#555" stroke-width="1.5"/></svg>
  <div class="circle" style="left:633px;top:2887px"><svg width="12" height="12" viewBox="0 0 12 12"><path d="M4 1l5 5-5 5" fill="none" stroke="#222" stroke-width="1.5"/></svg></div>

  <div class="tcard" style="left:123px;background:#111"><div class="abs" style="left:10px;top:10px;right:10px;bottom:10px;border:1px solid #777"></div>
    <p>Lorem ipsum dolor sit amet, consectetur adipiscing elit, sed do eiusmod tempor incididunt ut labore et dolore magna aliqua. Quis ipsum suspendisse ultrices gravida. Risus commodo viverra maecenas accumsan lacus vel facilisis.</p>
    <div class="avatar" role="img" aria-label="Customer portrait"></div><div class="who">Marco Velden</div><div class="role">Artist</div><div class="quote">”</div></div>
  <div class="tcard" style="left:545px;background:var(--grey)">
    <p>Lorem ipsum dolor sit amet, consectetur adipiscing elit, sed do eiusmod tempor incididunt ut labore et dolore magna aliqua. Quis ipsum suspendisse ultrices gravida. Risus commodo viverra maecenas accumsan lacus vel facilisis.</p>
    <div class="avatar" role="img" aria-label="Customer portrait"></div><div class="who">Marco Velden</div><div class="role">Artist</div><div class="quote">”</div></div>
  <div class="tcard" style="left:966px;width:234px;background:var(--grey);overflow:hidden">
    <p style="width:345px">Lorem ipsum dolor sit amet, consectetur adipiscing elit, sed do eiusmod tempor incididunt ut labore et dolore magna aliqua. Quis ipsum suspendisse ultrices gravida. Risus commodo viverra maecenas accumsan lacus vel facilisis.</p>
    <div class="avatar" role="img" aria-label="Customer portrait"></div><div class="who">Marco Velden</div><div class="role">Artist</div></div>
</section>

<!-- HOW IT WORKS -->
<section aria-label="How it works">
  <div class="abs" style="left:0;top:3246px;width:1200px;height:347px;background:var(--black)"></div>
  <h2 class="abs h" style="left:0;top:3302px;width:1200px;text-align:center;font-size:36px;letter-spacing:1.5px">How It Works</h2>
  <div class="step" style="left:111px"><svg viewBox="0 0 44 44" fill="var(--gold)"><rect x="8" y="12" width="22" height="16" rx="2"/><path d="M30 16h6l5 6v6h-11z"/><circle cx="15" cy="31" r="4"/><circle cx="34" cy="31" r="4"/><rect x="2" y="15" width="5" height="2"/><rect x="0" y="20" width="7" height="2"/></svg><h3>FREE SHIPPING</h3><p>Lorem ipsum dolor sit amet, consectetur adipiscing elit, sed do eiusmod tempor incididunt ut labore et dolore magna aliqua.</p></div>
  <div class="step" style="left:371px"><svg viewBox="0 0 44 44" fill="none" stroke="var(--gold)" stroke-width="3"><circle cx="24" cy="25" r="14"/><path d="M24 25V16M20 6h8M24 6v5" /><path d="M24 11a14 14 0 0 1 0 28z" fill="var(--gold)"/></svg><h3>60 DAY WARRANTY</h3><p>Lorem ipsum dolor sit amet, consectetur adipiscing elit, sed do eiusmod tempor incididunt ut labore et dolore magna aliqua.</p></div>
  <div class="step" style="left:630px"><svg viewBox="0 0 44 44" fill="none" stroke="var(--gold)" stroke-width="3"><path d="M22 4l16 8v18l-16 9-16-9V12z"/><path d="M6 12l16 9 16-9M22 21v18"/></svg><h3>EASY RETURNS</h3><p>Lorem ipsum dolor sit amet, consectetur adipiscing elit, sed do eiusmod tempor incididunt ut labore et dolore magna aliqua.</p></div>
  <div class="step" style="left:889px"><svg viewBox="0 0 44 44" fill="var(--gold)"><path d="M22 8h14l4 4v24H22l-6-8v-8z"/><rect x="4" y="24" width="10" height="14"/><circle cx="31" cy="14" r="2" fill="#0e0e0e"/></svg><h3>BEST PRICES</h3><p>Lorem ipsum dolor sit amet, consectetur adipiscing elit, sed do eiusmod tempor incididunt ut labore et dolore magna aliqua.</p></div>
</section>

<!-- NEWSLETTER -->
<section class="abs news" aria-label="Newsletter"></section>
<h2 class="abs h" style="left:0;top:3645px;width:1200px;text-align:center;font-size:36px;color:#111;letter-spacing:2px">Subscribe Our Newsletter</h2>
<p class="abs" style="left:350px;top:3705px;width:500px;text-align:center;font-size:10px;line-height:1.5;color:#3a2e10">Lorem ipsum dolor sit amet, consectetur adipiscing elit, sed do eiusmod tempor incididunt ut labore et dolore magna aliqua. Quis ipsum suspendisse ultrices gravida.</p>
<div class="field" style="left:344px">Name</div>
<div class="field" style="left:609px">Email</div>
<div class="abs" style="left:534px;top:3811px;width:132px;height:38px;background:var(--white);color:#111;font-size:11px;font-weight:700;display:flex;align-items:center;justify-content:center">SUBSCRIBE</div>

<!-- FOOTER -->
<footer aria-label="Footer">
  <div class="abs" style="left:0;top:3899px;width:1200px;height:317px;background:var(--coal)"></div>
  <div class="abs brand" style="top:3990px;left:123px"><i></i>Ironvale Locker</div>
  <p class="abs" style="left:123px;top:4048px;width:240px;font-size:11px;line-height:2.2;color:#e6e6e6">Lorem ipsum dolor sit amet, consectetur adipiscing elit, sed do eiusmod tempor incididunt ut labore..</p>

  <div class="fhead" style="left:512px">Quick Link</div>
  <div class="flink" style="left:512px;top:3979px">Home</div>
  <div class="flink" style="left:512px;top:4010px">Men's Jewelry</div>
  <div class="flink" style="left:512px;top:4041px">Cigar &amp; Bar Products</div>
  <div class="flink" style="left:512px;top:4072px">Man Cave Swag</div>
  <div class="flink" style="left:512px;top:4103px">Contact Us</div>

  <div class="fhead" style="left:755px">Follow Us</div>
  <div class="fdot" style="left:755px;top:3982px"></div><div class="flink" style="left:783px;top:3979px">Friendnet</div>
  <div class="fdot" style="left:755px;top:4013px"></div><div class="flink" style="left:783px;top:4010px">Chirper</div>
  <div class="fdot" style="left:755px;top:4044px"></div><div class="flink" style="left:783px;top:4041px">Snapframe</div>
  <div class="fdot" style="left:755px;top:4075px"></div><div class="flink" style="left:783px;top:4072px">Workline</div>

  <div class="fhead" style="left:958px">Address</div>
  <div class="flink" style="left:958px;top:3979px">48 Ashford Lane</div>
  <div class="flink" style="left:958px;top:4010px">Postal code- 482-190</div>
  <div class="flink" style="left:958px;top:4041px">Call - 404-718-295</div>

  <div class="abs" style="left:100px;top:4166px;width:1000px;height:1px;background:var(--gold-dark)"></div>
  <div class="abs" style="left:0;top:4186px;width:1200px;text-align:center;font-size:11px;color:#e6e6e6">Copyright ©&nbsp; 2023 Ironvale Locker. All rights reserved.</div>
</footer>

</body>
</html>
```